Business card for auto dealership

Looking for a clean modern design.
Would like attached logo incorporated

Industry/Entity Type

Car dealership

Contact Information for Business Card

Name, website, phone, cell, fax, email

```html
<!DOCTYPE html>
<html lang="en">
<head>
<meta charset="utf-8">
<title>Halvorsen Truck &amp; Auto Sales – Business Card</title>
<link href="https://fonts.googleapis.com/css2?family=Arimo:wght@400;700&display=swap" rel="stylesheet">
<style>
  :root {
    --stage: #2b2b2d;
    --card: #0b0b0c;
    --card-glow: #1d1d20;
    --ink: #ffffff;
    --ink-soft: #d9d9d9;
  }
  * { margin: 0; padding: 0; box-sizing: border-box; }
  html, body { width: 1200px; height: 874px; overflow: hidden; }
  body {
    background: var(--stage);
    font-family: "Arimo", Arial, sans-serif;
    color: var(--ink);
    position: relative;
  }
  .card {
    position: absolute;
    left: 310px;
    width: 580px;
    height: 332px;
    background: var(--card);
    overflow: hidden;
    box-shadow: 0 10px 30px rgba(0,0,0,0.45);
  }
  .card--front { top: 68px; }
  .card--back  { top: 474px; }
  .card__texture {
    position: absolute; inset: 0;
    background: radial-gradient(ellipse at 50% 55%, var(--card-glow) 0%, var(--card) 70%);
  }
  .brand {
    position: absolute;
    font-weight: 700;
    color: var(--ink);
    text-align: right;
    line-height: 1;
  }
  .brand__name { display: block; }
  .brand__tagline { display: block; text-transform: uppercase; letter-spacing: 0.04em; }
  .card--front .brand { right: 120px; top: 118px; }
  .card--front .brand__name { font-size: 62px; }
  .card--front .brand__tagline { font-size: 15px; margin-top: 8px; }
  .card--back .brand { right: 36px; bottom: 40px; }
  .card--back .brand__name { font-size: 40px; }
  .card--back .brand__tagline { font-size: 11px; margin-top: 6px; }
  .person { position: absolute; left: 46px; top: 56px; }
  .person__name { font-size: 19px; font-weight: 700; text-transform: uppercase; letter-spacing: 0.02em; }
  .person__role { font-size: 13px; color: var(--ink-soft); margin-top: 4px; }
  .contacts { position: absolute; left: 28px; bottom: 30px; list-style: none; }
  .contacts__item {
    display: flex; align-items: center; gap: 8px;
    font-size: 14px; line-height: 20px; color: var(--ink-soft);
  }
  .contacts__icon { width: 12px; height: 12px; fill: var(--ink); flex: none; }
</style>
</head>
<body>

<section class="card card--front">
  <div class="card__texture" role="img" aria-label="Dark perforated grille texture"></div>
  <div class="brand">
    <span class="brand__name">Halvorsen</span>
    <span class="brand__tagline">Truck &amp; Auto Sales</span>
  </div>
</section>

<section class="card card--back">
  <div class="card__texture" role="img" aria-label="Dark perforated grille texture"></div>
  <div class="person">
    <p class="person__name">Jordan Halvorsen</p>
    <p class="person__role">Managing Director</p>
  </div>
  <ul class="contacts">
    <li class="contacts__item">
      <svg class="contacts__icon" viewBox="0 0 12 12"><path d="M2 0.5 L4 0.5 L5 3 L3.6 4.2 Q4.6 6.6 7.8 8.4 L9 7 L11.5 8 L11.5 10 Q11 11.5 9.5 11.5 Q1 10.5 0.5 2.5 Q0.5 0.8 2 0.5Z"/></svg>
      555-014-2201
    </li>
    <li class="contacts__item">
      <svg class="contacts__icon" viewBox="0 0 12 12"><path d="M3 0 H9 V12 H3Z M4 1.5 V9 H8 V1.5Z"/><circle cx="6" cy="10.5" r="0.7" fill="#0b0b0c"/></svg>
      555-019-3376
    </li>
    <li class="contacts__item">
      <svg class="contacts__icon" viewBox="0 0 12 12"><path d="M3 0 H9 V4 H3Z M0.5 4.5 H11.5 V10 H9.5 V12 H2.5 V10 H0.5Z"/></svg>
      555-016-8842
    </li>
    <li class="contacts__item">
      <svg class="contacts__icon" viewBox="0 0 12 12"><path d="M0.5 2 H11.5 V10 H0.5Z"/><path d="M0.8 2.4 L6 6.5 L11.2 2.4" stroke="#0b0b0c" stroke-width="1" fill="none"/></svg>
      jordan@halvorsenauto.com
    </li>
    <li class="contacts__item">
      <svg class="contacts__icon" viewBox="0 0 12 12"><circle cx="6" cy="6" r="5.5"/><path d="M0.5 6 H11.5 M6 0.5 Q3 6 6 11.5 Q9 6 6 0.5" stroke="#0b0b0c" stroke-width="0.8" fill="none"/></svg>
      www.halvorsenauto.com
    </li>
  </ul>
  <div class="brand">
    <span class="brand__name">Halvorsen</span>
    <span class="brand__tagline">Truck &amp; Auto Sales</span>
  </div>
</section>

</body>
</html>
```